Business Card Design and Stationary design for consulting firm

Harbourline Sourcing are looking for a new business card design and a design for their A4 letterhead / A4 invoices.

We are seeking to heavily increase our brand awareness and require a business card that's professional in appearance but also shows flare and innovation. A card design that people will remember.

About Us
Harbourline Sourcing are `The Sourcing Crew’.
Our mission is to be one of Australia’s greatest companies. Our aim is to help our customers achieve the best result from their purchasing experience.

Our Requirement:
• IMPACT! IMPACT! IMPACT!
• BUSINESS & PROFESSIONAL LOOKING

• Our business colours are orange, blue and green (See the logo attached).

We have provided an Art Design specification (attached) that needs to be followed for you to win the design. This also has the font, which is used on the logo.

We are after a two sided business card

Side One should have the:
The company Logo
The Sourcing Crew
www.harbourlinesourcing.com.au
Procure | Personnel | Probity & Privacy
Sydney | Melbourne | Adelaide | Brisbane

Side Two
Logo (optional)
Harbourline Sourcing (optional)
Employee details (details listed below)

The above format is our preferred option, but if you think you can come up with something better, feel free to put it forward.

We are leaving the design up to you, but it must incorporate the logo.

We will need a template that we can change the employee details on, as we will be adding more staff over the coming months.

The details below are for one employee per card with the same design.
------------------------

Employee Details:

Marcus Del Arroyo MBA, MMgmtStratProc
Principal Consultant
0491 372 618
Marcus@harbourlinesourcing.com.au

Brianna Tolley
Consulting Manager
0462 915 308
Brianna@harbourlinesourcing.com.au

Our website is www.harbourlinesourcing.com.au

The Letterhead / invoice needs to incorporate:
the company Logo
The Sourcing Crew
Sydney | Melbourne | Adelaide | Brisbane but otherwise the design is over to you.

This file needs to be delivered in word format as other detail will be added to the documents.

We look forward to you award winning designs. If you require any further information please feel free to contact us.

Regards
Harbourline Sourcing

Target Market(s)

Our Target market is companies with 80+ employees. The market we segment is heavily male based, between the ages of 35-55 years of age.

Industry/Entity Type

Consulting

Contact Information for Business Card

See Project Description

Font styles to use
Other font styles liked:
• See Art Specification

Requirements
Must have
• Company Colours, See Project Description
Should not have
• Be outside the Art specification guidelines

```html
<!DOCTYPE html>
<html lang="en">
<head>
<meta charset="utf-8">
<title>Harbourline Sourcing – Business Card</title>
<link rel="stylesheet" href="https://fonts.googleapis.com/css2?family=Source+Sans+3:wght@400;600&display=swap">
<style>
  :root {
    --stage: #4a4a4a;
    --card: #000000;
    --white: #ffffff;
    --blue: #1b8fd6;
    --blue-light: #3aa6e6;
    --orange: #f26b21;
    --rule: #c4461a;
    --grey: #b8b8b8;
  }
  * { margin: 0; padding: 0; box-sizing: border-box; }
  html, body { width: 1200px; height: 750px; overflow: hidden; }
  body {
    background: var(--stage);
    font-family: "Source Sans 3", sans-serif;
    color: var(--white);
    position: relative;
  }
  .card {
    position: absolute;
    top: 228px;
    width: 462px;
    height: 263px;
    background: var(--card);
    overflow: hidden;
    text-align: center;
  }
  .card--contact { left: 124px; }
  .card--brand { left: 618px; }

  .wordmark {
    position: absolute;
    left: 0; right: 0;
    display: flex;
    flex-direction: column;
    align-items: center;
    font-weight: 600;
    color: var(--white);
    line-height: 1;
  }
  .wordmark__dot {
    width: 34px; height: 34px;
    border-radius: 50%;
    background: var(--blue);
    margin-bottom: 14px;
  }
  .wordmark__name { font-size: 26px; letter-spacing: 2px; }
  .wordmark__sub { font-size: 11px; letter-spacing: 3.5px; margin-top: 4px; }
  .card--contact .wordmark { top: 38px; }
  .card--brand .wordmark { top: 44px; }
  .card--brand .wordmark__name { font-size: 28px; }

  .person__name {
    position: absolute; top: 147px; left: 0; right: 0;
    color: var(--blue); font-size: 17px; font-weight: 600;
  }
  .person__creds { font-size: 12.5px; }
  .person__role {
    position: absolute; top: 169px; left: 29px; right: 29px;
    display: flex; align-items: center; gap: 6px;
    color: var(--orange); font-size: 12.5px;
  }
  .person__role::before, .person__role::after {
    content: ""; flex: 1; height: 1px; background: var(--rule);
  }
  .contact {
    position: absolute; top: 193px; left: 0; right: 0;
    display: flex; justify-content: center; align-items: center; gap: 7px;
    font-size: 12.5px;
  }
  .contact__item { display: flex; align-items: center; gap: 4px; }
  .website {
    position: absolute; left: 0; right: 0;
    color: var(--orange); font-size: 12.5px; letter-spacing: 2px;
  }
  .card--contact .website { top: 213px; }
  .card--brand .website { top: 225px; }
  .band {
    position: absolute; left: 0; right: 0; bottom: 0; height: 13px;
    background: linear-gradient(90deg, var(--blue), var(--blue-light) 70%, var(--blue));
  }

  .tagline {
    position: absolute; top: 160px; left: 0; right: 0;
    color: var(--blue); font-size: 17px; font-weight: 600;
  }
  .list {
    position: absolute; left: 0; right: 0; font-size: 12.5px;
  }
  .list--services { top: 186px; }
  .list--cities { top: 203px; }
  .list .sep { color: var(--blue); margin: 0 4px; }
</style>
</head>
<body>

<section class="card card--contact">
  <div class="wordmark">
    <span class="wordmark__dot"></span>
    <span class="wordmark__name">HARBOURLINE</span>
    <span class="wordmark__sub">SOURCING</span>
  </div>
  <p class="person__name">Marcus Del Arroyo <span class="person__creds">MBA, MMgmtStratProc</span></p>
  <p class="person__role">Principal Consultant</p>
  <div class="contact">
    <span class="contact__item">
      <svg width="9" height="13" viewBox="0 0 9 13" aria-hidden="true"><rect x="0.8" y="0.8" width="7.4" height="11.4" rx="1.2" fill="none" stroke="#f26b21" stroke-width="1.6"/><rect x="3" y="9.5" width="3" height="1.2" fill="#f26b21"/></svg>
      0491 372 618
    </span>
    <span class="contact__item">
      <svg width="12" height="9" viewBox="0 0 12 9" aria-hidden="true"><rect width="12" height="9" fill="#f26b21"/><path d="M0.5 0.8 L6 5 L11.5 0.8" fill="none" stroke="#000" stroke-width="1"/></svg>
      Marcus@harbourlinesourcing.com.au
    </span>
  </div>
  <p class="website">www.harbourlinesourcing.com.au</p>
  <div class="band"></div>
</section>

<section class="card card--brand">
  <div class="wordmark">
    <span class="wordmark__dot"></span>
    <span class="wordmark__name">HARBOURLINE</span>
    <span class="wordmark__sub">SOURCING</span>
  </div>
  <p class="tagline">The Sourcing Crew</p>
  <p class="list list--services">Procure<span class="sep">•</span>Personnel<span class="sep">•</span>Probity &amp; Privacy</p>
  <p class="list list--cities">Sydney<span class="sep">•</span>Melbourne<span class="sep">•</span>Adelaide<span class="sep">•</span>Brisbane</p>
  <p class="website">www.harbourlinesourcing.com.au</p>
</section>

</body>
</html>
```